Layout für unsere Stellenanzeigen
Zielgruppe
Wir sind spezialisiert auf die Personalvermittlung von Medizinischen Fachkräften! Krankenschwestern - Altenpfleger u.s.w....!
Aufgabenstellung
Es soll nicht überladen sein - gerne kreativ witzig. Bitte einmal über unsere Homepage schauen. Wir arbeiten mit den Farben grün grau und schwarz. Pantonen anbei! Wir haben unsere Stil komplett auf Strichmännchen - Cartoon ausgelegt. Vielleicht gibt es hier Ideen diese Strichmännchen mit Realen Bilder zu kombinieren!!??!
Anlage:

```html
<!DOCTYPE html>
<html lang="de">
<head>
<meta charset="utf-8">
<title>Stellenanzeige – Pflegekraft Plus</title>
<link rel="stylesheet" href="https://fonts.googleapis.com/css2?family=Ubuntu:wght@300;400;700&family=Fira+Sans:wght@400;600&family=Caveat:wght@500&display=swap">
<style>
  :root {
    --green: #3a9a3e;
    --green-light: #5cb85a;
    --green-dark: #2a7a2f;
    --green-text: #2ea03a;
    --grey: #6b6a6f;
    --white: #ffffff;
    --page: #f3f3f1;
  }
  * { margin: 0; padding: 0; box-sizing: border-box; }
  html, body { width: 1200px; height: 817px; overflow: hidden; background: var(--page); }
  .ad {
    position: absolute; left: 320px; top: 12px;
    width: 560px; height: 793px;
    background: var(--white);
    font-family: "Fira Sans", sans-serif;
    overflow: hidden;
    box-shadow: 0 2px 10px rgba(0,0,0,.12);
  }
  .url-band {
    height: 38px; background: var(--green);
    color: var(--white); font-family: "Ubuntu", sans-serif;
    font-size: 17px; letter-spacing: .5px;
    padding: 9px 0 0 28px;
  }
  .headline {
    height: 112px; padding: 12px 0 0 28px;
    font-family: "Ubuntu", sans-serif; font-weight: 300;
    color: var(--green-text); font-size: 37px; line-height: 44px;
    text-transform: uppercase; letter-spacing: .5px;
  }
  .headline strong { font-weight: 700; }
  .offer {
    position: absolute; left: 0; top: 150px; width: 560px; height: 305px;
    background: linear-gradient(160deg, var(--green-light) 0%, var(--green) 55%, var(--green-dark) 100%);
  }
  .offer-title {
    position: absolute; left: 28px; top: 30px;
    font-family: "Ubuntu", sans-serif; color: var(--white);
    font-size: 30px; line-height: 36px; letter-spacing: .5px;
  }
  .offer-title .light { font-weight: 300; }
  .offer-title b { font-weight: 700; text-transform: uppercase; }
  .tag-home-office {
    position: absolute; left: 236px; top: 255px;
    padding: 5px 16px;
    border: 2px dashed var(--white); border-radius: 16px;
    color: var(--white); font-family: "Ubuntu", sans-serif; font-size: 18px; font-weight: 300;
  }
  .illustration {
    position: absolute; left: 390px; top: 250px; width: 155px; height: 355px;
    background: linear-gradient(180deg, #f4f4f4 0%, #e4efe3 45%, #9fcf9c 100%);
    border-radius: 12px;
  }
  .copy { position: absolute; color: var(--green-text); font-size: 12.5px; line-height: 16px; font-weight: 600; }
  .copy-1 { left: 28px; top: 472px; width: 340px; }
  .copy-2 { left: 70px; top: 540px; width: 305px; }
  .footer {
    position: absolute; left: 0; top: 650px; width: 560px; height: 143px;
    background: var(--grey); color: var(--white);
  }
  .footer-note {
    position: absolute; left: 20px; top: 16px; width: 120px;
    font-family: "Caveat", cursive; font-size: 20px; line-height: 21px;
  }
  .brand {
    position: absolute; left: 150px; top: 22px; width: 130px;
    display: flex; align-items: center; gap: 8px;
    font-family: "Fira Sans", sans-serif; font-weight: 600; font-size: 15px; line-height: 17px;
  }
  .brand-dot { flex: none; width: 30px; height: 30px; border-radius: 50%; background: var(--white); }
  .divider { position: absolute; left: 290px; top: 14px; width: 1px; height: 104px; background: var(--white); }
  .address, .contact { position: absolute; left: 302px; width: 250px; font-size: 11px; line-height: 14px; }
  .address { top: 12px; }
  .contact { top: 76px; }
</style>
</head>
<body>
  <article class="ad">
    <div class="url-band">www.pflegekraft-plus.de</div>
    <h1 class="headline">Nicht nur <strong>Superhelden</strong><br>tragen einen <strong>Umhang.</strong></h1>

    <section class="offer">
      <h2 class="offer-title">
        <span class="light">Werde</span><br>
        <b>Gesundheits- und<br>Krankenpfleger/in</b><br>
        <span class="light">oder</span> <b>Kinderkranken-<br>pfleger/in!</b>
      </h2>
      <span class="tag-home-office">Home Office</span>
    </section>

    <div class="illustration" role="img" aria-label="Gezeichnete Strichfigur einer Pflegerin im grünen Kasack, die ein Herz hochhält"></div>

    <p class="copy copy-1">Sie sind verantwortungsbewusst, können selbstständig arbeiten, sind erfahren in der Pflege und im Umgang mit chronisch Kranken?</p>
    <p class="copy copy-2">Sie arbeiten gerne eigenverantwortlich von zu Hause aus, sind trotzdem reisefreudig (Ba-Wü), schätzen einen Dienstwagen der Mittelklasse – auch zur privaten Nutzung und suchen eine überwiegend organisatorische und beratende Tätigkeit, die spannend und gut bezahlt ist?</p>

    <footer class="footer">
      <p class="footer-note">Wir freuen uns auf Ihre Anfrage!</p>
      <div class="brand"><span class="brand-dot"></span><span>Pflegekraft Plus</span></div>
      <div class="divider"></div>
      <p class="address">Pflegekraft Plus Personaldienste GmbH<br>Jonas Berger<br>Lindenallee 12<br>79100 Musterstadt</p>
      <p class="contact">Tel: 0761 - 555 120 0 · Fax: 0761 - 555 120 9<br>Mobil: 0170 555 43 21<br>jonas.berger@pflegekraft-plus.de</p>
    </footer>
  </article>
</body>
</html>
```